Website design for an Online pastry shop

Website Name : www.lanternandreed.example

Description of the website and its target audience
We are a premium pastry company producing delicious cakes, macarons, cookies, gelato, and other sweet dessert. Our differentiation is that our products are freshly produced with premium quality imported ingredients and one bite into our products set us apart from other bakery shop. We online retail online so as to provide high quality products at a affordable cost. Our products has received raving reviews by many food enthusiast even the hard to please ones. The products contain more natural ingredients and we do not add preservatives. The return rates for our pastry is almost 80%. You only need to try once to be return customers. Our greatest challenge is getting customer to take the first bite. We are so sure of our products that we are going to give people free food tasting.

We are based in China but all our products are developed by award winning chefs from 5 stars hotel. The target customer is woman 16 to 40+ in china. Working class ladies and demand high quality products. A modern, sophisticated and minimalist website

This is a competitive market and image is crucial for such a food ‘conscious ’ orientated customer. They want to feel that they are buying from a reliable company that take great effort to ensure food cleaniness and safety yet affordable price. We make almost 98% of sub ingredients ourselves and we make it by hand.

Style/theme ideas for the web page design
I am looking for a elegant a little rustic, handmade feel yet sophisticated design - one that is easy to the eye yet functional and easy for the user to navigate through. Good play of fonts to give let it feel unique and customised. Black and white is our corporate colours. However, we do not want black background as it does not tease the taste bud. All our colours should come from our products. Customers should be very close to our products. They eat with their eyes first. Black and white is just accent.

Inspirational and competitors websites
http://www.48torte.example/ ( Key competitor )
I like the simple, clean look. The products are the key focus
https://www.plivva.example/
clean, fresh and different. Attractive with purpose. Feminine
http://quillandlattice.example/
this has a great layout - lots of information and nicely presented. Very sweet and feminine
http://www.shopharbourvelm.example/
product features is the focus
http://www.janeltorvick.example/store/
fun, feminine, rustic

Number of pages needed : 6 ( Uncoded PSD design only )
Page descriptions
Home Page - This page will show what makes our products stand out from the competitors and provide an introduction of who we are.
2nd page : Product catalogue
3nd page: Detail Product page with pictures and descriptions. Select products size and add to cart....
4rd page: Brand Story with pictures and descriptions.
5th page Contact Us : Here they can contact or schedule an appointment for free product tasting
6th page : Check out page

• See packaging

Requirements
Must have
• Please see the project wire frame file " main page.png " or file number 70

```html
<!DOCTYPE html>
<html lang="en">
<head>
<meta charset="utf-8">
<title>Lantern &amp; Reed — Home</title>
<link rel="stylesheet" href="https://fonts.googleapis.com/css2?family=Oswald:wght@400;500&family=Signika:wght@400;600;700&family=Mulish:wght@400;600&display=swap">
<style>
:root{
  --page-bg:#1f1f1f;
  --ink:#161616;
  --nav:#3b3b3b;
  --nav-dark:#2a2a2a;
  --tan:#c48b4d;
  --tan-light:#e6c07c;
  --brown:#8a5a2c;
  --brown-dark:#6e4420;
  --paper:#ffffff;
  --line:#d7d7d7;
  --muted:#666;
  --link:#2a9aa3;
}
*{box-sizing:border-box;margin:0;padding:0}
html,body{width:762px;height:1200px;overflow:hidden;background:var(--page-bg)}
.canvas{width:762px;height:1200px;overflow:hidden;position:relative}
.page{position:absolute;left:0;top:0;width:921px;height:1450px;transform:scale(.8274);transform-origin:0 0;background:var(--page-bg);font-family:"Mulish",sans-serif;color:var(--ink)}
.abs{position:absolute}

/* top strip */
.promo-tag{left:60px;top:25px;width:178px;height:22px;background:var(--tan-light);border-radius:3px 3px 0 0;font:600 10.5px/22px "Signika",sans-serif;text-align:center}
.account{right:59px;top:25px;height:22px;display:flex;background:var(--tan-light);border-radius:3px 3px 0 0;font:600 10.5px/22px "Signika",sans-serif}
.account span{padding:0 9px;border-left:1px solid #c9a461}
.account span:first-child{border-left:none}
.main-nav{left:44px;top:48px;width:834px;height:40px;background:linear-gradient(#4a4a4a,var(--nav-dark));display:flex;border-radius:3px 3px 0 0}
.main-nav a{color:#fff;text-decoration:none;font:600 14px/40px "Signika",sans-serif;text-align:center;border-right:1px solid #555}
.brand-tab{left:357px;top:0;width:208px;height:128px;background:var(--ink);border-radius:0 0 4px 4px;display:flex;align-items:flex-end;justify-content:center;padding-bottom:10px}
.brand-tab .brand-name{color:#fff;font:600 23px "Signika",sans-serif;letter-spacing:.5px}
.brand-tab .brand-mark{width:14px;height:14px;background:#fff;position:absolute;top:28px;left:97px}

/* hero */
.hero{left:44px;top:88px;width:834px;height:297px;background:var(--paper);border-bottom:3px solid var(--tan)}
.hero h1{position:absolute;left:56px;top:50px;font:500 64px/70px "Oswald",sans-serif;color:var(--tan);letter-spacing:-1px}
.hero p{position:absolute;left:59px;top:192px;font:700 14px/18px "Signika",sans-serif}
.btn-dark{position:absolute;left:56px;top:243px;width:100px;height:33px;background:var(--ink);color:#fff;font:400 18px/33px "Oswald",sans-serif;text-align:center;border-radius:2px}
.hero-photo{position:absolute;left:472px;top:46px;width:302px;height:232px;border-radius:50%/46%;background:radial-gradient(ellipse at 50% 30%,#f4efe9 0,#e9ddd0 40%,#c9633c 62%,#d9a06a 80%,#ecd3b0 100%)}
.arrow{position:absolute;width:32px;height:32px}

/* welcome + about */
.welcome{left:345px;top:395px;width:230px;height:56px;background:var(--brown);border-radius:0 0 14px 14px;text-align:center;color:#fff}
.welcome strong{display:block;font:700 32px/34px "Signika",sans-serif;margin-top:3px}
.welcome small{font:600 12px "Signika",sans-serif}
.about{left:65px;top:450px;width:800px;height:185px;background:var(--paper);border-radius:30px 18px 28px 16px;text-align:center}
.about h2{position:absolute;left:28px;top:16px;font:700 30px "Signika",sans-serif;color:var(--tan)}
.about p{position:absolute;left:18px;right:18px;top:57px;font:400 12px/18px "Mulish",sans-serif}
.btn-tan{position:absolute;background:var(--tan);color:#fff;text-align:center;border-radius:2px}
.about .btn-tan{left:673px;top:154px;width:77px;height:25px;font:400 15px/25px "Oswald",sans-serif}

/* testimonials */
.section-title{color:#fff;font:600 18px "Signika",sans-serif;text-align:center;width:921px;left:0}
.avatar{left:234px;top:690px;width:96px;height:96px;border-radius:50%;border:4px solid #fff;background:linear-gradient(#bdbdbd,#6d6d6d)}
.person{left:204px;top:796px;width:160px;text-align:center;color:#fff;font:600 16px "Signika",sans-serif}
.quote{left:402px;top:693px;width:305px;height:90px;background:var(--paper);border-radius:8px;padding:9px 14px;font:400 8.6px/11.2px "Mulish",sans-serif}
.quote::before{content:"";position:absolute;left:-12px;top:38px;border:8px solid transparent;border-right:6px solid var(--paper);border-left:none}
.dots{left:432px;top:812px;display:flex;gap:3px}
.dots i{width:8px;height:8px;border-radius:50%;background:#666}
.dots i:first-child{background:#999}

/* products */
.products{left:38px;top:828px;width:842px;height:380px;background:var(--paper);border-radius:6px 10px 4px 8px}
.tape{position:absolute;width:44px;height:18px;background:#e3c98f;opacity:.9}
.products h2{position:absolute;left:51px;top:22px;font:600 14px "Signika",sans-serif;color:var(--tan)}
.products .more{position:absolute;right:36px;top:27px;font:400 9px "Signika",sans-serif;color:var(--tan)}
.products .lead{position:absolute;left:55px;top:49px;font:400 10px "Signika",sans-serif;color:#333}
.card{position:absolute;top:83px;width:185px;height:275px;border:1px solid #bbb;border-radius:3px;overflow:hidden;background:#fff}
.card .photo{height:199px;background:linear-gradient(170deg,#4a2a1c 0,#6b3a24 35%,#efe6d4 55%,#a6672f 70%,#6d4025 100%)}
.card .name{position:absolute;left:11px;top:206px;font:400 14px "Oswald",sans-serif;color:var(--tan)}
.card .price{position:absolute;right:10px;top:205px;font:700 14px "Signika",sans-serif}
.qty{position:absolute;left:11px;top:239px;right:10px;height:20px;display:flex;align-items:center;font:400 11px "Oswald",sans-serif}
.qty .label{width:56px}
.qty .step{width:18px;height:18px;border:1px solid var(--line);color:var(--tan);font:700 15px/16px "Signika",sans-serif;text-align:center}
.qty .num{width:28px;height:18px;border-top:1px solid var(--line);border-bottom:1px solid var(--line);text-align:center;font:400 9px/17px "Mulish",sans-serif}
.qty .add{margin-left:6px;width:38px;height:20px;background:var(--tan);color:#fff;font:400 9px/20px "Signika",sans-serif;text-align:center;border-radius:2px}

/* subscribe + tweets */
.subscribe{left:74px;top:1256px;width:393px;height:90px;background:var(--brown);border-radius:3px}
.subscribe::after{content:"";position:absolute;inset:5px;border:1px dashed #d9b37c}
.subscribe h3{position:absolute;width:100%;top:10px;text-align:center;color:#fff;font:600 19px "Signika",sans-serif}
.email{position:absolute;left:24px;top:38px;width:335px;height:40px;background:#fff;border-radius:5px;font:400 14px/40px "Mulish",sans-serif;color:#aaa;padding-left:14px;z-index:1}
.email b{position:absolute;right:4px;top:4px;width:32px;height:32px;background:var(--tan);border-radius:3px}
.tweets{left:498px;top:1256px;width:304px;height:90px;background:var(--paper);border-radius:10px;display:flex;gap:14px;padding:8px 12px}
.tweets p{width:132px;font:400 8.7px/11px "Mulish",sans-serif}
.tweets a{color:var(--link);text-decoration:none}
.tweets em{display:block;text-align:right;padding-right:14px;margin-top:4px;font-size:8.7px}
.social-dot{left:826px;top:1283px;width:36px;height:36px;border-radius:50%;background:#fff}
.footer-name{left:0;width:921px;top:1362px;text-align:center;color:#fff;font:700 26px "Signika",sans-serif}
.footer{left:0;top:1410px;width:921px;height:40px;background:#fff;font:600 8.5px/40px "Mulish",sans-serif}
.footer nav{position:absolute;left:127px}
.footer nav span{margin:0 9px;color:#333}
.footer nav span:first-child{margin-left:0}
.follow{position:absolute;left:677px;display:flex;align-items:center;gap:4px}
.follow i{width:21px;height:21px;display:inline-block}
</style>
</head>
<body>
<div class="canvas">
<div class="page">

  <div class="abs promo-tag">Free Delivery for Orders above - 50$</div>
  <div class="abs account"><span>Log in</span><span>Sign Up</span><span>My Cart</span></div>

  <nav class="abs main-nav">
    <a style="width:83px">Cake</a><a style="width:123px">Macarons</a><a style="width:100px">Cookies</a>
    <span style="width:215px"></span>
    <a style="width:97px;border-left:1px solid #555">Gelato</a><a style="width:125px">Tasting Room</a><a style="width:91px;border-right:none">About Us</a>
  </nav>
  <div class="abs brand-tab"><span class="brand-mark"></span><span class="brand-name">Lantern &amp; Reed</span></div>

  <section class="abs hero">
    <h1>A NEW LEVEL<br>OF PASTRY !!</h1>
    <p>We Value flavor over fuss. Artisan, Handcrated<br>&amp; other direct to your door.</p>
    <div class="btn-dark">LEARN MORE</div>
    <div class="hero-photo" role="img" aria-label="Large macaron sandwich filled with scoops of gelato"></div>
    <svg class="arrow" style="left:6px;top:124px" viewBox="0 0 32 32"><circle cx="16" cy="16" r="14" fill="#fff" stroke="#888" stroke-width="2"/><path d="M8 16l6-6v4h9v4h-9v4z" fill="none" stroke="#555" stroke-width="1.6"/></svg>
    <svg class="arrow" style="left:789px;top:124px" viewBox="0 0 32 32"><circle cx="16" cy="16" r="14" fill="#fff" stroke="#888" stroke-width="2"/><path d="M24 16l-6-6v4H9v4h9v4z" fill="none" stroke="#555" stroke-width="1.6"/></svg>
  </section>

  <div class="abs welcome"><strong>WELCOME</strong><small>to our website</small></div>

  <section class="abs about">
    <h2>ABOUT</h2>
    <p>Lorem Ipsum is simply dummy text of the printing and typesetting industry. Lorem Ipsum has been the industry's standard dummy text ever since the 1500s, when an unknown printer took a galley of type and scrambled it to make a type specimen book. It has survived not only five centuries, but also the leap into electronic typesetting, remaining essentially unchange Lorem Ipsum is simply dummy text of the printing and typesetting ndustry. Lorem Ipsum has been the industry's tandard dummy text ever since the 1500s, Lorem Ipsum is simply dummy text of the printing and typesetting industry. Lorem Ipsum has been the industry's standard dummy text ever since the 1500s,</p>
    <div class="btn-tan">LEARN MORE</div>
  </section>

  <h2 class="abs section-title" style="top:647px">Testimonials</h2>
  <svg class="arrow abs" style="left:77px;top:729px" viewBox="0 0 32 32"><circle cx="16" cy="16" r="14" fill="#2a2a2a" stroke="#999" stroke-width="2"/><path d="M8 16l6-6v4h9v4h-9v4z" fill="none" stroke="#ccc" stroke-width="1.6"/></svg>
  <svg class="arrow abs" style="left:804px;top:729px" viewBox="0 0 32 32"><circle cx="16" cy="16" r="14" fill="#2a2a2a" stroke="#999" stroke-width="2"/><path d="M24 16l-6-6v4H9v4h9v4z" fill="none" stroke="#ccc" stroke-width="1.6"/></svg>
  <div class="abs avatar" role="img" aria-label="Customer portrait photo"></div>
  <div class="abs person">Name Here</div>
  <blockquote class="abs quote">Lorem Ipsum is simply dummy text of the printing and typesetting industry. Lorem Ipsum has been the industry's standard dummy text ever since the 1500s, when an unknown printer took a galley of type and scrambled it to make a type specimen book.Lorem Ipsum is simply dummy text of the printing and typesetting industry. Lorem Ipsum has been the industry's standard dummy text ever since the 1500s,</blockquote>
  <div class="abs dots"><i></i><i></i><i></i><i></i><i></i></div>

  <section class="abs products">
    <span class="tape" style="left:-6px;top:2px;transform:rotate(-30deg)"></span>
    <span class="tape" style="right:-6px;top:-2px;transform:rotate(30deg)"></span>
    <span class="tape" style="left:-6px;bottom:2px;transform:rotate(30deg)"></span>
    <span class="tape" style="right:-6px;bottom:2px;transform:rotate(-30deg)"></span>
    <h2>Our Products</h2>
    <span class="more">view our full product range &gt;&gt;</span>
    <p class="lead">Lorem Ipsum is simply dummy text of the printing and typesetting industry. Lorem Ipsum has been the industry's standard dummy text ever since the 1500s,</p>

    <article class="card" style="left:35px"><div class="photo" role="img" aria-label="Chocolate layer cake topped with chocolate shavings"></div><span class="name">Cake</span><span class="price">$0.00</span><div class="qty"><span class="label">Quantity</span><span class="step">–</span><span class="num">1</span><span class="step">+</span><span class="add">Add</span></div></article>
    <article class="card" style="left:234px"><div class="photo" role="img" aria-label="Chocolate layer cake topped with chocolate shavings"></div><span class="name">Cake</span><span class="price">$0.00</span><div class="qty"><span class="label">Quantity</span><span class="step">–</span><span class="num">1</span><span class="step">+</span><span class="add">Add</span></div></article>
    <article class="card" style="left:433px"><div class="photo" role="img" aria-label="Chocolate layer cake topped with chocolate shavings"></div><span class="name">Cake</span><span class="price">$0.00</span><div class="qty"><span class="label">Quantity</span><span class="step">–</span><span class="num">1</span><span class="step">+</span><span class="add">Add</span></div></article>
    <article class="card" style="left:631px"><div class="photo" role="img" aria-label="Chocolate layer cake topped with chocolate shavings"></div><span class="name">Cake</span><span class="price">$0.00</span><div class="qty"><span class="label">Quantity</span><span class="step">–</span><span class="num">1</span><span class="step">+</span><span class="add">Add</span></div></article>
  </section>

  <section class="abs subscribe">
    <h3>Subcribe to the Lantern and Reed</h3>
    <div class="email">Please Enter your email address<b><svg width="32" height="32" viewBox="0 0 32 32"><path d="M13 10l6 6-6 6" fill="none" stroke="#fff" stroke-width="3"/></svg></b></div>
  </section>

  <section class="abs tweets">
    <p>Lorem Ipsum is simply dummy text of the printing and typese tting industry. Lorem Ipsum has been the. <a>http://yoursite.example/subdomain</a><em>1st jan, 12:00pm</em></p>
    <p>Lorem Ipsum is simply dummy text of the printing and typese tting industry. Lorem Ipsum has been the. <a>http://yoursite.example/subdomain</a><em>1st jan, 12:00pm</em></p>
  </section>
  <div class="abs social-dot"></div>

  <div class="abs footer-name">Lantern &amp; Reed</div>

  <footer class="abs footer">
    <nav><span>About Us</span>|<span>Contact Us</span>|<span>Privacy Policy</span>|<span>Terms &amp; Conditions</span>|<span>Site Map</span></nav>
    <div class="follow">Folow Us: <i style="background:#3b5a9a;margin-left:14px"></i><i style="background:#2aa3dc"></i><i style="background:#c4302b"></i></div>
  </footer>

</div>
</div>
</body>
</html>
```